Business Card Design Project

Doctor, Pain Management. Need a new business card design with appointment info on the back. New address is 18 Whitcombe Road, Suite 305, Manalapan, NJ 07726. Right now I believe the rest of the information is staying the same.

```html
<!DOCTYPE html>
<html lang="en">
<head>
<meta charset="utf-8">
<title>Evenkeel Pain Management – Business Card</title>
<link href="https://fonts.googleapis.com/css2?family=Libre+Baskerville:wght@700&family=Poppins:wght@400;500;600;700&display=swap" rel="stylesheet">
<style>
  :root {
    --stage: #2b2b2b;
    --olive-dark: #2f2e24;
    --cream: #f3e6d7;
    --taupe: #b2a698;
    --paper: #f6f5f1;
    --ink: #1d1c18;
    --yellow: #ede43a;
    --rule: #8e8d86;
  }
  * { box-sizing: border-box; margin: 0; padding: 0; }
  html, body { width: 1200px; height: 1200px; overflow: hidden; }
  body {
    background: var(--stage);
    font-family: "Poppins", sans-serif;
    color: var(--ink);
    position: relative;
  }
  .card {
    position: absolute;
    left: 150px;
    width: 900px;
    height: 514px;
    border-radius: 34px;
    overflow: hidden;
  }
  .card--front { top: 56px; background: var(--cream); }
  .card--back { top: 630px; background: var(--olive-dark); }
  .card-shape { position: absolute; inset: 0; width: 100%; height: 100%; }

  /* Front */
  .doctor {
    position: absolute;
    right: 60px;
    top: 52px;
    text-align: right;
  }
  .doctor-name {
    font-family: "Libre Baskerville", serif;
    font-weight: 700;
    font-size: 40px;
    letter-spacing: 0.5px;
    line-height: 1;
  }
  .doctor-name .degrees { font-size: 19px; letter-spacing: 0; }
  .doctor-title { font-size: 19px; margin-top: 6px; }
  .contact-block {
    position: absolute;
    right: 60px;
    text-align: right;
    font-size: 17px;
    line-height: 1.55;
  }
  .contact-block b { font-weight: 600; }
  .contact-phones { top: 170px; }
  .contact-address { top: 268px; }
  .contact-web { top: 378px; }
  .brand {
    position: absolute;
    left: 56px;
    top: 330px;
    display: flex;
    align-items: center;
    gap: 16px;
  }
  .brand-dot {
    width: 34px; height: 34px;
    border-radius: 50%;
    background: var(--yellow);
    flex: none;
  }
  .brand-name {
    color: var(--yellow);
    font-weight: 500;
    font-size: 30px;
    line-height: 1.2;
  }

  /* Back */
  .appointment-title {
    position: absolute;
    left: 0; right: 0;
    top: 22px;
    text-align: center;
    color: var(--yellow);
    font-weight: 700;
    font-size: 46px;
  }
  .appointment-form {
    position: absolute;
    left: 0; right: 0;
    top: 104px;
    height: 256px;
    background: var(--paper);
    padding: 28px 50px 0;
  }
  .form-row { display: flex; align-items: flex-end; gap: 14px; }
  .form-label { font-weight: 500; font-size: 26px; line-height: 1; }
  .form-line { flex: 1; border-bottom: 1.5px solid var(--rule); height: 22px; }
  .days {
    display: flex;
    justify-content: space-between;
    margin: 30px 10px 26px 40px;
  }
  .day { display: flex; align-items: center; gap: 10px; font-size: 21px; font-weight: 500; }
  .day-box { width: 30px; height: 30px; border: 2px solid var(--ink); }
  .form-note {
    font-size: 15px;
    margin: 8px 0 0 120px;
  }
  .back-contacts {
    position: absolute;
    left: 0; right: 0;
    top: 380px;
    text-align: center;
    color: #fff;
    font-size: 25px;
    line-height: 1.65;
  }
  .back-contacts .key { color: var(--yellow); }
  .back-contacts .sep { margin: 0 14px; }
</style>
</head>
<body>

<section class="card card--front" aria-label="Front side">
  <svg class="card-shape" viewBox="0 0 900 514" preserveAspectRatio="none" aria-hidden="true">
    <path d="M0 200 C 200 150, 400 200, 500 320 C 550 385, 580 450, 600 514 L0 514 Z" fill="var(--taupe)"/>
    <path d="M0 222 C 190 175, 380 225, 470 340 C 515 400, 540 460, 555 514 L0 514 Z" fill="var(--olive-dark)"/>
  </svg>

  <div class="doctor">
    <h1 class="doctor-name">LIANWEI ZHOU<span class="degrees">, M.D., Ph.D</span></h1>
    <p class="doctor-title">Board Certified Anesthesiologist</p>
  </div>

  <p class="contact-block contact-phones"><b>P:</b> 555.204.3187<br><b>F:</b> 555.204.3188</p>
  <p class="contact-block contact-address">18 Whitcombe Road, Suite 305<br>Manalapan, NJ 07726</p>
  <p class="contact-block contact-web"><b>E:</b> hello@evenkeelpain.com<br><b>W:</b> www.evenkeelpain.com</p>

  <div class="brand">
    <span class="brand-dot" aria-hidden="true"></span>
    <p class="brand-name">Evenkeel<br>Pain Management</p>
  </div>
</section>

<section class="card card--back" aria-label="Back side">
  <h2 class="appointment-title">Appointment</h2>

  <div class="appointment-form">
    <div class="form-row">
      <span class="form-label">For:</span><span class="form-line"></span>
    </div>
    <div class="days">
      <span class="day"><span class="day-box"></span>Mon</span>
      <span class="day"><span class="day-box"></span>Tue</span>
      <span class="day"><span class="day-box"></span>Wed</span>
      <span class="day"><span class="day-box"></span>Thu</span>
      <span class="day"><span class="day-box"></span>Fri</span>
      <span class="day"><span class="day-box"></span>Sat</span>
      <span class="day"><span class="day-box"></span>Sun</span>
    </div>
    <div class="form-row">
      <span class="form-label">Date:</span><span class="form-line"></span>
    </div>
    <p class="form-note">if you are unable to keep your appointment, please contact us as soon as possible</p>
  </div>

  <div class="back-contacts">
    <p><span class="key">P:</span> 555.204.3187<span class="sep">|</span><span class="key">F:</span> 555.204.3188</p>
    <p><span class="key">E:</span> hello@evenkeelpain.com<span class="sep">|</span><span class="key">W:</span> evenkeelpain.com</p>
  </div>
</section>

</body>
</html>
```